Construction material supplies company business card ****

1. Full company name “Marlow Aggregate Products Ltd”
I am after a Business card design for the company as a whole. We are better known in Solomon Islands as “Marlow Aggregate” for short.

We are a building materials supplier of
Ready Mixed Concrete, Bricks and Blocks,
Quarry products- gravel, aggregates, sand etc.
Cement distributor/retailer of reputable brands.
Other prefab concrete products. Culverts, wave breakers, concrete retaining blocks etc.

2. Competitive Advantage over Competition: Quality, efficient, professional, dependable, reliable

3. We want people to feel trust worthy, high quality, strong when they see our brand

5. No preference to color. Maybe more sturdy and corporate. Not fancy.

Industry/Entity Type

CONSTRUCTION SUPPLY

Contact Information for Business Card

Name, Position, office phone mob phone, email

Requirements
Must have
• the company logo
Nice to have
• would like to see a mixture of designs, of with logo only and also with simple graphic designs to bring out the company whilst still have the strong sturdy professional feeling

```html
<!DOCTYPE html>
<html lang="en">
<head>
<meta charset="utf-8">
<title>Marlow Aggregate – Business Card</title>
<link rel="stylesheet" href="https://fonts.googleapis.com/css2?family=Archivo:wght@800&family=Arimo:wght@400&display=swap">
<style>
  :root {
    --backdrop: #2b2c2e;
    --card: #1c1d1f;
    --card-back-top: #2a2b2e;
    --card-back-bottom: #151618;
    --brand-blue: #1f4e7a;
    --text-light: #e9eaec;
    --rule: #2f4a48;
  }
  * { box-sizing: border-box; margin: 0; padding: 0; }
  html, body {
    width: 1200px;
    height: 1108px;
    overflow: hidden;
    background: var(--backdrop);
  }
  .sheet {
    position: relative;
    width: 1200px;
    height: 1108px;
  }
  .card {
    position: absolute;
    top: 214px;
    width: 440px;
    height: 680px;
    border-radius: 26px;
    box-shadow: 0 14px 30px rgba(0,0,0,0.45);
    overflow: hidden;
  }
  .card-front {
    left: 120px;
    background: var(--card);
    display: flex;
    flex-direction: column;
    align-items: center;
    text-align: center;
  }
  .brand {
    margin-top: 150px;
    display: flex;
    align-items: center;
    gap: 14px;
    font-family: "Archivo", sans-serif;
    font-weight: 800;
    font-size: 34px;
    line-height: 1.05;
    letter-spacing: 1px;
    text-transform: uppercase;
    color: var(--brand-blue);
  }
  .brand-square {
    width: 26px;
    height: 26px;
    background: var(--brand-blue);
    flex: none;
  }
  .contact {
    margin-top: auto;
    margin-bottom: 86px;
  }
  .person-name {
    font-family: "Archivo", sans-serif;
    font-weight: 800;
    font-size: 27px;
    letter-spacing: 0.5px;
    text-transform: uppercase;
    color: var(--brand-blue);
  }
  .person-role {
    margin-top: 4px;
    font-family: "Arimo", sans-serif;
    font-size: 21px;
    color: var(--text-light);
  }
  .divider {
    width: 110px;
    height: 1px;
    background: var(--rule);
    margin: 16px auto 14px;
  }
  .contact-line {
    font-family: "Arimo", sans-serif;
    font-size: 21px;
    line-height: 1.3;
    color: var(--text-light);
  }
  .card-back {
    left: 640px;
  }
  .back-surface {
    position: absolute;
    inset: 0;
    width: 100%;
    height: 100%;
  }
  .back-brand {
    position: absolute;
    left: 0;
    right: 0;
    top: 470px;
    text-align: center;
    font-family: "Archivo", sans-serif;
    font-weight: 800;
    font-size: 16px;
    letter-spacing: 1px;
    text-transform: uppercase;
    color: var(--brand-blue);
  }
</style>
</head>
<body>
<main class="sheet">
  <section class="card card-front" aria-label="Card front">
    <div class="brand">
      <span class="brand-square" aria-hidden="true"></span>
      <span>Marlow<br>Aggregate</span>
    </div>
    <div class="contact">
      <p class="person-name">Daniel Harper</p>
      <p class="person-role">Managing Director</p>
      <div class="divider"></div>
      <p class="contact-line">044-555 210 347</p>
      <p class="contact-line">044-555 210 347</p>
      <p class="contact-line">info@marlowaggregate.sb</p>
    </div>
  </section>

  <section class="card card-back" aria-label="Card back">
    <svg class="back-surface" viewBox="0 0 440 680" preserveAspectRatio="none" role="img" aria-label="Repeating tone-on-tone brand pattern across the card back">
      <defs>
        <linearGradient id="backTone" x1="0" y1="0" x2="0.4" y2="1">
          <stop offset="0" stop-color="var(--card-back-top)"/>
          <stop offset="1" stop-color="var(--card-back-bottom)"/>
        </linearGradient>
      </defs>
      <rect width="440" height="680" fill="url(#backTone)"/>
    </svg>
    <p class="back-brand">Marlow Aggregate</p>
  </section>
</main>
</body>
</html>
```